Kerno Solutions: searching for a flyer to trow in letterboxes for properties we are interested in

Hello ,

Introduction:
We are a company based in Luxembourg called "Kerno Solutions". We are specialized in buying properties on which we develop and build constructions before selling them.

Informations for the flyer:
We need a flyer to trow into the letter boxes of property owners letting them know that we are interested in buying their property, if they are interested they can give us a call.

The text for the flyer/letter is in the attachment called >>2020-03-11_KS_Text for flyer,letter there might be slight changes<<.

We need to look competent, professional and financially stable.

The flyer needs to be short and not over welling with information otherwise it will land in the trash.

We have decided that we don't want real pictures on the flyer, but shapes of any kind, blue prints, drawings are fine.

Format should be in DIN A4. We plan to print the flyer on both sides in two different languages, in other words the design will be the same on both sides only the text will be in a different language.

I also added our current logo and here is the design of the website that is under construction at the moment http://www.kernosolutions-example.lu/. The logo's color can be changed into a different blue or uni color (all white or all black).
Updates

Hi, First time user the howl thing started faster as expected. Furthermore, I need to catch my boss to discust the project with him and he is on a lot of meetings. Please give us a little bit more time. Thanks

Target Market(s)

Property owners

Requirements
Must have
• email, phone number, tax number (RCS), Tax number , matriculation and address.
see word file in attachment for information
Nice to have
• Our company logo, in one form or an other, you can be creative, the logo is in the attachment.
Should not have
• Real pictures

```html
<!DOCTYPE html>
<html lang="fr">
<head>
<meta charset="utf-8">
<title>Kerno Solutions – Flyer</title>
<link href="https://fonts.googleapis.com/css2?family=Arimo:wght@400&family=Oswald:wght@500&display=swap" rel="stylesheet">
<style>
  :root {
    --backdrop: #6b6b6b;
    --paper: #ffffff;
    --brand-blue: #0a6594;
    --brand-blue-deep: #06507a;
    --band-black: #1b1b1b;
    --band-grey: #3a3a3a;
    --ink: #141414;
    --city-light: #f4f4f4;
    --city-mid: #c9c9c9;
  }
  * { margin: 0; padding: 0; box-sizing: border-box; }
  html, body { width: 1200px; height: 1200px; overflow: hidden; }
  body { background: var(--backdrop); position: relative; font-family: "Arimo", Arial, sans-serif; color: var(--ink); }

  .flyer {
    position: absolute; top: 234px; width: 524px; height: 734px;
    background: var(--paper); overflow: hidden;
    box-shadow: 0 2px 6px rgba(0,0,0,.35);
  }
  .flyer--fr { left: 66px; }
  .flyer--lb { left: 622px; }

  .flyer__shapes { position: absolute; inset: 0; width: 100%; height: 100%; }

  .brand { position: absolute; left: 38px; top: 114px; }
  .brand__mark { width: 52px; height: 52px; background: var(--brand-blue); margin-left: 44px; margin-bottom: 20px; }
  .brand__name {
    font-family: "Oswald", "Arial Narrow", sans-serif; font-weight: 500;
    font-size: 26px; line-height: 1; letter-spacing: .3px; color: var(--brand-blue);
    text-transform: uppercase;
  }

  .contact { position: absolute; left: 38px; top: 242px; list-style: none; font-size: 11.6px; line-height: 14.4px; }
  .contact__item { display: flex; align-items: flex-start; gap: 6px; margin-bottom: 6px; }
  .contact__item svg { width: 10px; height: 10px; margin-top: 2px; flex: none; }

  .letter { position: absolute; left: 41px; font-size: 11.6px; line-height: 14.4px; }
  .flyer--fr .letter { top: 341px; width: 440px; }
  .flyer--lb .letter { top: 348px; width: 470px; }
  .letter p { margin-bottom: 14.4px; }

  .skyline {
    position: absolute; left: 0; right: 0; top: 496px; bottom: 0;
    background: linear-gradient(180deg, var(--paper) 0%, var(--city-light) 25%, var(--city-mid) 100%);
  }
</style>
</head>
<body>

<article class="flyer flyer--fr" lang="fr">
  <div class="skyline" role="img" aria-label="Silhouette grise d'une ville en construction avec grues et échafaudages"></div>
  <svg class="flyer__shapes" viewBox="0 0 654 917" preserveAspectRatio="none" aria-hidden="true">
    <defs>
      <linearGradient id="blueFr" x1="0" y1="0" x2="1" y2="1"><stop offset="0" stop-color="#0a6594"/><stop offset="1" stop-color="#06507a"/></linearGradient>
      <linearGradient id="blackFr" x1="0" y1="0" x2="0" y2="1"><stop offset="0" stop-color="#3a3a3a"/><stop offset="1" stop-color="#111"/></linearGradient>
    </defs>
    <polygon points="0,0 654,0 654,210 585,257 145,60 0,175" fill="url(#blueFr)"/>
    <polygon points="12,0 654,150 654,210 585,257 145,60" fill="url(#blackFr)"/>
    <polygon points="0,803 440,917 0,917" fill="url(#blueFr)"/>
    <polygon points="185,850 232,822 470,917 400,917" fill="url(#blackFr)"/>
  </svg>

  <header class="brand">
    <div class="brand__mark"></div>
    <div class="brand__name">Kerno Solutions</div>
  </header>

  <ul class="contact">
    <li class="contact__item">
      <svg viewBox="0 0 10 10"><path d="M5 0.5a3.3 3.3 0 0 0-3.3 3.3C1.7 6.3 5 9.6 5 9.6s3.3-3.3 3.3-5.8A3.3 3.3 0 0 0 5 .5z" fill="var(--brand-blue)"/><circle cx="5" cy="3.8" r="1.2" fill="#fff"/></svg>
      <span>18 rue du Chantier, L-3290<br>Bettembourg</span>
    </li>
    <li class="contact__item">
      <svg viewBox="0 0 10 10"><rect x=".5" y="2" width="9" height="6" fill="var(--brand-blue)"/><path d="M.5 2 5 5.5 9.5 2" stroke="#fff" stroke-width=".8" fill="none"/></svg>
      <span>info@kernosolutions-example.lu</span>
    </li>
    <li class="contact__item">
      <svg viewBox="0 0 10 10"><circle cx="5" cy="5" r="4.4" stroke="var(--brand-blue)" stroke-width=".8" fill="none"/><path d="M3.4 2.8c-.4.4 0 2 1.2 3.1s2.5 1.5 2.9 1.1l.3-.6-1-.7-.5.4c-.6-.2-1.3-.9-1.5-1.5l.4-.5-.7-1z" fill="var(--brand-blue)"/></svg>
      <span>691 000 482</span>
    </li>
  </ul>

  <section class="letter">
    <p>Madame/Monsieur,</p>
    <p>Ce courrier vous a été adressé, car votre propriété a attiré notre attention. Nous souhaiterions discuter avec vous de son éventuel rachat par notre société.</p>
    <p>En cas d'accord, nous vous assurons une décision rapide, un paiement garanti, et zéro frais d'intermédiaire.</p>
    <p>En attendant de vos nouvelles, nous restons à votre entière disposition pour tout renseignement.</p>
    <p>Salutations distinguées,</p>
    <p>L'équipe de Kerno Solutions</p>
  </section>
</article>

<article class="flyer flyer--lb" lang="lb">
  <div class="skyline" role="img" aria-label="Gro Silhouette vun enger Stad am Bau mat Kranen a Gerüster"></div>
  <svg class="flyer__shapes" viewBox="0 0 654 917" preserveAspectRatio="none" aria-hidden="true">
    <defs>
      <linearGradient id="blueLb" x1="0" y1="0" x2="1" y2="1"><stop offset="0" stop-color="#0a6594"/><stop offset="1" stop-color="#06507a"/></linearGradient>
      <linearGradient id="blackLb" x1="0" y1="0" x2="0" y2="1"><stop offset="0" stop-color="#3a3a3a"/><stop offset="1" stop-color="#111"/></linearGradient>
    </defs>
    <polygon points="0,0 654,0 654,222 598,257 145,60 0,183" fill="url(#blueLb)"/>
    <polygon points="26,0 654,146 654,222 598,257 145,60" fill="url(#blackLb)"/>
    <polygon points="0,803 440,917 0,917" fill="url(#blueLb)"/>
    <polygon points="185,850 232,822 470,917 400,917" fill="url(#blackLb)"/>
  </svg>

  <header class="brand">
    <div class="brand__mark"></div>
    <div class="brand__name">Kerno Solutions</div>
  </header>

  <ul class="contact">
    <li class="contact__item">
      <svg viewBox="0 0 10 10"><path d="M5 0.5a3.3 3.3 0 0 0-3.3 3.3C1.7 6.3 5 9.6 5 9.6s3.3-3.3 3.3-5.8A3.3 3.3 0 0 0 5 .5z" fill="var(--brand-blue)"/><circle cx="5" cy="3.8" r="1.2" fill="#fff"/></svg>
      <span>18 rue du Chantier, L-3290<br>Bettembourg</span>
    </li>
    <li class="contact__item">
      <svg viewBox="0 0 10 10"><rect x=".5" y="2" width="9" height="6" fill="var(--brand-blue)"/><path d="M.5 2 5 5.5 9.5 2" stroke="#fff" stroke-width=".8" fill="none"/></svg>
      <span>info@kernosolutions-example.lu</span>
    </li>
    <li class="contact__item">
      <svg viewBox="0 0 10 10"><circle cx="5" cy="5" r="4.4" stroke="var(--brand-blue)" stroke-width=".8" fill="none"/><path d="M3.4 2.8c-.4.4 0 2 1.2 3.1s2.5 1.5 2.9 1.1l.3-.6-1-.7-.5.4c-.6-.2-1.3-.9-1.5-1.5l.4-.5-.7-1z" fill="var(--brand-blue)"/></svg>
      <span>691 000 482</span>
    </li>
  </ul>

  <section class="letter">
    <p>Madame / Monsieur,</p>
    <p>Dir kritt dëst Schreiwes well Är Proprietéit eis Opmierksamkeet zeréckbehalen huet.<br>Mir géinge gär mat Iech iwwert d'Méiglechkeet, datt eise Betrib se opkeeft, diskutéieren.</p>
    <p>Mir versécheren Iech e séieren Entscheedungsprozess, garantéieren d'Bezuelung a verrechne keng Drëttkäschten.</p>
    <p>Mir géingen eis freeën, vun Iech ze héieren, a sti ganz zu Ärer Verfügung fir zousätzlech Informatiounen.</p>
    <p>Mat beschte Gréiss,</p>
    <p>D'Equipe vun Kerno Solutions</p>
  </section>
</article>

</body>
</html>
```